RM Cargoline businesscard project

RM Cargoline Ltd is a freshly founded small (3 employees), young (average age is 30 years) company, living from the road transportation market without own tools.
We would like to have an impressive, new-line, cool busines card for a freshly founded forwarding company on an overcrowded market which raises attention and makes the potential partners eager to work with us.

Target Market(s)

The main profile of the company is logistic/forwarding on road.

Industry/Entity Type

Freight Forwarding

Contact Information for Business Card

Name: Berki Zsófia
Title: general manager
mobile nr: +36-70/482-5193
fax nr: +36-1/534-9061
e-mail: zsofia.berki@rmcargoline.example
info@rmcargoline.example
website address: http://www.rmcargoline.example
and if possible maybe some funny or helpful info on the back

Requirements
Must have
• contact details above
Nice to have
• some really nice and catching back-side (info, graphics, useful tool info... anything)
Should not have
• trucks, road, ship, airplane on it...

```html
<!DOCTYPE html>
<html lang="en">
<head>
<meta charset="utf-8">
<title>RM Cargoline – Business Card</title>
<link rel="stylesheet" href="https://fonts.googleapis.com/css2?family=Roboto+Condensed:wght@400&family=Open+Sans:wght@400;600&display=swap">
<style>
  :root {
    --page-bg: #e9e9e7;
    --card-white: #f7f7f6;
    --band-light: #7bbbdc;
    --band-mid: #5b9bc9;
    --band-deep: #3e74ad;
    --stripe-dark: #3a3b3d;
    --ink: #3b3b3d;
    --accent: #5a9fd0;
    --on-band: #ffffff;
  }
  * { margin: 0; padding: 0; box-sizing: border-box; }
  html, body { width: 1200px; height: 780px; overflow: hidden; }
  body { background: var(--page-bg); position: relative; font-family: "Open Sans", Arial, sans-serif; }

  .card {
    position: absolute; left: 100px; top: 105px;
    width: 1000px; height: 570px;
    background: var(--card-white);
    box-shadow: 0 6px 22px rgba(0,0,0,.18);
    overflow: hidden;
  }
  .card__wave { position: absolute; inset: 0; width: 100%; height: 100%; }

  .holder { position: absolute; right: 56px; top: 48px; text-align: right; color: var(--on-band); }
  .holder__name { font-family: "Open Sans", Arial, sans-serif; font-weight: 600; font-size: 40px; line-height: 1; }
  .holder__title { font-size: 22px; line-height: 1.2; margin-top: 4px; opacity: .95; }

  .brand { position: absolute; left: 70px; bottom: 70px; display: flex; align-items: center; gap: 22px; }
  .brand__square { width: 54px; height: 54px; background: var(--accent); }
  .brand__name { font-family: "Roboto Condensed", Arial, sans-serif; font-weight: 400; font-size: 76px; line-height: 1; color: var(--ink); }

  .contacts { position: absolute; left: 560px; top: 300px; }
  .contacts__web { font-size: 22px; color: var(--accent); margin-bottom: 10px; }
  .contacts__list { list-style: none; }
  .contacts__item { display: flex; align-items: center; gap: 12px; font-size: 22px; color: var(--ink); line-height: 1.55; }
  .contacts__icon { width: 26px; height: 26px; flex: none; }
</style>
</head>
<body>
  <section class="card" aria-label="RM Cargoline business card, front">
    <svg class="card__wave" viewBox="0 0 1000 570" preserveAspectRatio="none" aria-hidden="true">
      <defs>
        <linearGradient id="bandGradient" x1="0" y1="1" x2="1" y2="0">
          <stop offset="0" stop-color="var(--band-deep)"/>
          <stop offset=".55" stop-color="var(--band-light)"/>
          <stop offset="1" stop-color="var(--band-mid)"/>
        </linearGradient>
      </defs>
      <path d="M0 0 H1000 V200 C820 210 720 240 600 300 C460 370 320 350 0 395 Z" fill="url(#bandGradient)"/>
      <path d="M1000 200 C820 210 720 240 600 300 C460 370 320 350 0 395" fill="none" stroke="var(--stripe-dark)" stroke-width="22"/>
    </svg>

    <div class="holder">
      <p class="holder__name">Berki Zsófia</p>
      <p class="holder__title">general manager</p>
    </div>

    <div class="contacts">
      <p class="contacts__web">www.rmcargoline.example</p>
      <ul class="contacts__list">
        <li class="contacts__item">
          <svg class="contacts__icon" viewBox="0 0 26 26" aria-label="mobile"><rect width="26" height="26" fill="var(--accent)"/><rect x="9" y="5" width="8" height="16" rx="1.5" fill="none" stroke="#fff" stroke-width="1.8"/><line x1="12" y1="18" x2="14" y2="18" stroke="#fff" stroke-width="1.6"/></svg>
          +36-70/482-5193
        </li>
        <li class="contacts__item">
          <svg class="contacts__icon" viewBox="0 0 26 26" aria-label="fax"><rect width="26" height="26" fill="var(--accent)"/><rect x="8" y="5" width="10" height="6" fill="none" stroke="#fff" stroke-width="1.6"/><rect x="5" y="11" width="16" height="8" fill="#fff"/><rect x="8" y="16" width="10" height="5" fill="var(--accent)" stroke="#fff" stroke-width="1.4"/></svg>
          +36-1/534-9061
        </li>
        <li class="contacts__item">
          <svg class="contacts__icon" viewBox="0 0 26 26" aria-label="e-mail"><rect width="26" height="26" fill="var(--accent)"/><rect x="5" y="7" width="16" height="12" fill="none" stroke="#fff" stroke-width="1.6"/><path d="M5 7 L13 14 L21 7" fill="none" stroke="#fff" stroke-width="1.6"/></svg>
          zsofia.berki@rmcargoline.example
        </li>
        <li class="contacts__item">
          <svg class="contacts__icon" viewBox="0 0 26 26" aria-label="e-mail"><rect width="26" height="26" fill="var(--accent)"/><rect x="5" y="7" width="16" height="12" fill="none" stroke="#fff" stroke-width="1.6"/><path d="M5 7 L13 14 L21 7" fill="none" stroke="#fff" stroke-width="1.6"/></svg>
          info@rmcargoline.example
        </li>
      </ul>
    </div>

    <div class="brand">
      <span class="brand__square" aria-hidden="true"></span>
      <span class="brand__name">RM Cargoline</span>
    </div>
  </section>
</body>
</html>
```